Eye Catching Business Card for Optometrist

We've recently refreshed our logo and now we need a fresh and bold look for our business cards. We provide progressive ways to improve people's vision and protect their eye health.

Use our new logo as guidance into the colors to use. As far as style goes, I love how bold and eye catching the card is for Lanternfly Studio. Feel free to use your creative judgement.

Tagline: "Clearly the best for your vision."

pertinent info to include:

Dr. Martin Sowerby
Optometrist

2857 Bramwell Ridge Blvd #217
Marlowe Springs, MO 64012
(555) 382-7190

marty@brightlenshomeoptics.example
www.brightlenshomeoptics.example

```html
<!DOCTYPE html>
<html lang="en">
<head>
<meta charset="utf-8">
<title>Brightlens Home Optics – Business Card</title>
<link rel="stylesheet" href="https://fonts.googleapis.com/css2?family=Lato:wght@400;700;900&display=swap">
<style>
  :root {
    --bg: #dde8ef;
    --card-front: #f4f4f4;
    --card-back: #e1e1e1;
    --red: #c9252e;
    --brown: #6a5444;
    --tan: #d6bb97;
    --faint-grey: #d3d0cf;
    --faint-red: #e0d0cd;
  }
  * { box-sizing: border-box; margin: 0; padding: 0; }
  html, body { width: 1200px; height: 960px; overflow: hidden; }
  body {
    background: var(--bg);
    font-family: "Lato", Arial, sans-serif;
    position: relative;
  }
  .card {
    position: absolute;
    left: 294px;
    width: 614px;
    height: 352px;
    overflow: hidden;
  }
  .card-front { top: 102px; background: var(--card-front); }
  .card-back { top: 510px; background: var(--card-back); }

  .brand {
    position: absolute;
    left: 0; right: 0;
    display: flex;
    align-items: center;
    justify-content: center;
    gap: 14px;
  }
  .brand-mark {
    width: 44px; height: 44px;
    background: var(--red);
    flex: none;
  }
  .brand-name {
    color: var(--red);
    font-weight: 900;
    font-size: 30px;
    line-height: 1.02;
    letter-spacing: 0.5px;
    text-transform: uppercase;
  }
  .card-front .brand { top: 62px; }
  .card-back .brand { top: 222px; }

  .person {
    position: absolute;
    left: 88px;
    top: 216px;
  }
  .person-name {
    color: var(--brown);
    font-weight: 700;
    font-size: 18px;
  }
  .person-role {
    color: var(--red);
    font-size: 14px;
    margin-top: 8px;
  }
  .divider {
    position: absolute;
    left: 304px;
    top: 186px;
    width: 2px;
    height: 118px;
    background: var(--red);
  }
  .contact {
    position: absolute;
    right: 36px;
    top: 208px;
    text-align: right;
    color: var(--red);
    font-size: 13.5px;
    line-height: 18px;
  }
  .contact-address { margin-right: 0; margin-bottom: 7px; }
  .contact-line {
    display: flex;
    justify-content: flex-end;
    align-items: center;
    gap: 6px;
  }
  .contact-line svg { width: 12px; height: 12px; flex: none; }
  .band {
    position: absolute;
    left: 0; right: 0;
    top: 326px;
    height: 16px;
    display: flex;
  }
  .band-brown { width: 308px; background: var(--brown); }
  .band-tan { flex: 1; background: var(--tan); }

  .backdrop-name {
    position: absolute;
    left: 0; right: 0;
    top: 26px;
    text-align: center;
    font-size: 62px;
    line-height: 1.1;
    text-transform: uppercase;
  }
  .backdrop-top { display: block; color: var(--faint-grey); font-weight: 400; }
  .backdrop-bottom { display: block; color: var(--faint-red); font-weight: 900; }
</style>
</head>
<body>
  <section class="card card-front">
    <div class="brand">
      <span class="brand-mark"></span>
      <span class="brand-name">Brightlens<br>Home Optics</span>
    </div>
    <div class="person">
      <p class="person-name">Dr. Martin Sowerby</p>
      <p class="person-role">Optometrist</p>
    </div>
    <div class="divider"></div>
    <div class="contact">
      <p class="contact-address">2857 Bramwell Ridge Blvd #217<br>Marlowe Springs, MO 64012</p>
      <p class="contact-line">(555) 382-7190
        <svg viewBox="0 0 12 12" aria-hidden="true"><rect x="3" y="0.5" width="6" height="11" rx="1" fill="none" stroke="#6a5444" stroke-width="1.2"/><circle cx="6" cy="9.5" r="0.7" fill="#6a5444"/></svg>
      </p>
      <p class="contact-line">marty@brightlenshomeoptics.example
        <svg viewBox="0 0 12 12" aria-hidden="true"><rect x="0.5" y="2" width="11" height="8" fill="#6a5444"/><path d="M0.5 2 L6 6.5 L11.5 2" fill="none" stroke="#f4f4f4" stroke-width="1"/></svg>
      </p>
      <p class="contact-line">www.brightlenshomeoptics.example
        <svg viewBox="0 0 12 12" aria-hidden="true"><rect x="0.6" y="1" width="10.8" height="7.5" fill="none" stroke="#6a5444" stroke-width="1.2"/><rect x="4" y="9.5" width="4" height="1.5" fill="#6a5444"/></svg>
      </p>
    </div>
    <div class="band"><span class="band-brown"></span><span class="band-tan"></span></div>
  </section>

  <section class="card card-back">
    <p class="backdrop-name" aria-hidden="true"><span class="backdrop-top">Brightlens</span><span class="backdrop-bottom">Home Optics</span></p>
    <div class="brand">
      <span class="brand-mark"></span>
      <span class="brand-name">Brightlens<br>Home Optics</span>
    </div>
  </section>
</body>
</html>
```